New website for out outstanding veterinary training center

We already have a beautiful logo with nice colors and we are now looking for a breathtaking modern website to present our training center and future corses held there. A section to book open courses should also be available.

We are planing the realize the website with Wordpress.
The following pages should be available:
- Startpage / Overview
- Page to present the different rooms and seating option
- Page where the rooms can be booked
- Page where recommended accommodation are presented
- Page to present and book corses
- contact page
- Impressum

Target Market(s)

European Union

Industry/Entity Type

Education, Veterinary medicine

Number of Pages Required

5+ page

Font styles to use
Sans Serif

Colors
00AB8E
00BBA5
67D7C9
C6EFE9
E9F9F6

Requirements
Must have
• The website must be clear and easy to read. The colors form the logos should be used for the design.
Should not have
• To playful design. The page is not for a veterinary practice. we are a training center for veterinarians!

```html
<!DOCTYPE html>
<html lang="en">
<head>
<meta charset="utf-8">
<title>Veterra Training Center</title>
<link rel="stylesheet" href="https://fonts.googleapis.com/css2?family=Lato:wght@400;700;900&display=swap">
<style>
:root{
  --teal:#1DB394;
  --teal-deep:#1B8076;
  --teal-dark:#1A776D;
  --mint:#B6EAE3;
  --mint-soft:#C6EFE9;
  --mint-pale:#E9F9F6;
  --plum:#3D2F3D;
  --plum-footer:#3F2E3E;
  --text:#4A3F4A;
  --white:#ffffff;
}
*{box-sizing:border-box;margin:0;padding:0}
html,body{width:1200px;height:4850px;overflow:hidden}
body{font-family:'Lato',sans-serif;color:var(--text);background:var(--white);position:relative}
.abs{position:absolute}
.btn{position:absolute;display:flex;align-items:center;justify-content:center;background:var(--teal);color:var(--white);font-weight:700;border-radius:30px;font-size:17px}
.section-title{position:absolute;left:0;width:1200px;text-align:center;font-weight:700;color:var(--plum);font-size:42px}
.rule{position:absolute;height:4px;width:76px;background:var(--teal-deep);left:562px}
.photo{position:absolute;border-radius:6px}

/* top bar */
.topbar{position:absolute;left:0;top:0;width:1200px;height:57px;background:var(--mint-pale)}
.social{position:absolute;top:19px;display:flex;gap:18px}
.social span{width:20px;height:20px;border-radius:50%;background:var(--plum);display:block}
.nav{position:absolute;left:0;top:57px;width:1200px;height:113px;background:var(--white)}
.nav a{position:absolute;top:48px;font-size:16px;color:var(--plum);text-decoration:none;font-weight:700}
.brand{position:absolute;left:70px;top:20px;display:flex;align-items:center;gap:10px;z-index:2}
.brand .mark{width:70px;height:70px;border-radius:50%;background:var(--teal-deep);border:4px solid var(--white)}
.brand .name{font-weight:900;font-size:22px;color:var(--plum);line-height:1.1}

/* hero */
.hero{position:absolute;left:0;top:170px;width:1200px;height:690px;background:linear-gradient(120deg,#6d7f82 0%,#9aa9a8 35%,#c9c3b8 60%,#8f8d88 100%)}
.hero h1{position:absolute;left:0;top:180px;width:1200px;text-align:center;color:var(--white);font-size:68px;line-height:70px;font-weight:700}
.dots{position:absolute;top:612px;left:560px;display:flex;gap:14px}
.dots i{width:10px;height:10px;border-radius:50%;background:rgba(255,255,255,.5);display:block}
.dots i:first-child{background:var(--white)}

/* overview */
.overview h2{position:absolute;left:75px;top:980px;font-size:42px;color:var(--plum);font-weight:700}
.para{position:absolute;font-size:16px;line-height:31px;color:var(--text)}
.bigmark{position:absolute;left:663px;top:919px;width:464px;height:464px;border-radius:50%;border:22px solid var(--teal-deep);display:flex;align-items:center;justify-content:center}
.bigmark span{font-size:40px;font-weight:700;color:var(--teal-deep)}

/* cards */
.card-h{position:absolute;width:330px;text-align:center;font-size:22px;font-weight:700;color:var(--plum)}
.card-p{position:absolute;width:330px;text-align:center;font-size:16px;line-height:28px;color:var(--text)}

/* why */
.why{position:absolute;left:0;top:3382px;width:1200px;height:484px;background:linear-gradient(160deg,#1d8a7e,#176b63)}
.why h2{position:absolute;left:0;top:110px;width:1200px;text-align:center;font-size:48px;color:var(--white);font-weight:700;letter-spacing:1px}
.why .item{position:absolute;top:213px;width:200px;text-align:center}
.why .circle{width:124px;height:124px;border-radius:50%;background:var(--white);margin:0 auto;display:flex;align-items:center;justify-content:center}
.why .label{margin-top:20px;color:var(--white);font-size:22px;font-weight:700}

/* testimonials */
.tcard{position:absolute;top:4013px;width:330px;height:373px;background:var(--mint-pale)}
.tcard .q{position:absolute;left:0;top:-6px;font-size:48px;font-weight:900;color:var(--plum);font-family:Georgia,serif}
.tcard p{position:absolute;left:44px;top:52px;width:250px;font-size:15px;line-height:25px;color:var(--plum)}
.tcard .who{position:absolute;left:44px;top:302px;display:flex;align-items:center;gap:12px}
.tcard .avatar{width:40px;height:40px;border-radius:50%;background:#b9c2c5}
.tcard .who b{display:block;font-size:12px;font-weight:400}
.tcard .who small{font-size:12px}

/* footer */
.footer{position:absolute;left:0;top:4452px;width:1200px;height:398px;background:var(--plum-footer);color:var(--white)}
.footer h4{position:absolute;top:68px;font-size:24px;color:var(--teal);font-weight:700}
.footer ul{position:absolute;top:115px;list-style:none;font-size:16px;line-height:33px}
.footer .copy{position:absolute;font-size:16px;line-height:30px}
.fbrand{position:absolute;left:75px;top:130px;width:220px;text-align:center}
.fbrand .mark{width:100px;height:100px;border-radius:50%;border:6px solid var(--white);margin:0 auto 14px}
.fbrand .name{font-size:30px;font-weight:900;line-height:1.1}
.input{position:absolute;left:885px;top:169px;width:242px;height:46px;border-radius:23px;background:var(--white);color:var(--plum);font-size:16px;padding-left:18px;display:flex;align-items:center}
</style>
</head>
<body>

<header>
  <div class="topbar">
    <div class="social" style="left:772px">
      <span></span><span></span><span></span><span></span><span></span>
    </div>
    <div class="btn" style="left:980px;top:9px;width:147px;height:38px;font-size:14px">Book Course</div>
  </div>
  <nav class="nav">
    <a style="left:347px">Home</a>
    <a style="left:428px">About Us</a>
    <a style="left:537px">Rooms</a>
    <a style="left:625px">Book Course</a>
    <a style="left:759px">Accommodation</a>
    <a style="left:921px">Impressum</a>
    <a style="left:1042px">Contact Us</a>
  </nav>
  <div class="brand">
    <div class="mark"></div>
    <div class="name">Veterra<br>Training Center</div>
  </div>
</header>

<section class="hero" role="img" aria-label="Two veterinarians in scrubs examining a small white dog on a clinic table">
  <h1>Veterra<br>Training Center</h1>
  <div class="btn" style="left:511px;top:367px;width:177px;height:51px">Book Course</div>
  <div class="dots"><i></i><i></i><i></i><i></i></div>
  <svg class="abs" style="left:0;bottom:-2px" width="1200" height="80" viewBox="0 0 1200 80" preserveAspectRatio="none">
    <path d="M0,25 C250,85 420,85 600,55 C800,20 1000,10 1200,40 L1200,80 L0,80 Z" fill="#fff"/>
  </svg>
</section>

<section class="overview">
  <h2>Company Overview</h2>
  <div class="abs" style="left:75px;top:1046px;width:76px;height:4px;background:var(--teal-deep)"></div>
  <p class="para" style="left:75px;top:1066px;width:540px">Sed ut perspiciatis unde omnis iste natus error sit voluptatem accusantium doloremque laudantium, totam rem aperiam, eaque ipsa quae ab illo inventore veritatis et quasi architecto beatae vitae dicta sunt explicabo. Nemo enim ipsam voluptatem quia voluptas sit aspernatur aut odit aut fugit, sed quia consequuntur magni dolores eos qui ratione voluptatem sequi nesciunt.</p>
  <div class="btn" style="left:75px;top:1285px;width:179px;height:51px">Read More</div>
  <div class="bigmark"><span>Veterra</span></div>
</section>

<section class="courses">
  <div class="abs" style="left:0;top:1462px;width:1200px;height:660px;background:var(--mint)"></div>
  <svg class="abs" style="left:0;top:2110px" width="1200" height="50" viewBox="0 0 1200 50" preserveAspectRatio="none">
    <path d="M0,0 L1200,0 L1200,35 C1000,5 800,5 600,30 C420,50 200,45 0,20 Z" fill="#B6EAE3"/>
  </svg>
  <h2 class="section-title" style="top:1518px">Feature Courses</h2>
  <div class="rule" style="top:1586px"></div>

  <div class="photo" style="left:75px;top:1645px;width:330px;height:201px;background:linear-gradient(135deg,#cfd6c9,#9fae9a)" role="img" aria-label="Student reading a textbook next to an animal skeleton model"></div>
  <div class="photo" style="left:435px;top:1645px;width:330px;height:201px;background:linear-gradient(135deg,#eef0ec,#c9a27c)" role="img" aria-label="Veterinarian with stethoscope examining a dachshund"></div>
  <div class="photo" style="left:797px;top:1645px;width:330px;height:201px;background:linear-gradient(135deg,#e6e8ea,#aab2b8)" role="img" aria-label="Instructor presenting at a flip chart to a class"></div>

  <h3 class="card-h" style="left:75px;top:1864px">Course Heading</h3>
  <h3 class="card-h" style="left:435px;top:1864px">Course Heading</h3>
  <h3 class="card-h" style="left:797px;top:1864px">Course Heading</h3>
  <p class="card-p" style="left:75px;top:1900px">Sed ut perspiciatis unde omnis iste natus error sit voluptatem accusantium doloremque quaerat.</p>
  <p class="card-p" style="left:435px;top:1900px">Sed ut perspiciatis unde omnis iste natus error sit voluptatem accusantium doloremque quaerat.</p>
  <p class="card-p" style="left:797px;top:1900px">Sed ut perspiciatis unde omnis iste natus error sit voluptatem accusantium doloremque quaerat.</p>
  <div class="btn" style="left:151px;top:2003px;width:179px;height:51px">Book Course</div>
  <div class="btn" style="left:511px;top:2003px;width:179px;height:51px">Book Course</div>
  <div class="btn" style="left:872px;top:2003px;width:179px;height:51px">Book Course</div>
</section>

<section class="rooms">
  <h2 class="section-title" style="top:2228px">Rooms &amp; Seating Option</h2>
  <div class="rule" style="top:2296px"></div>

  <div class="photo" style="left:75px;top:2355px;width:330px;height:200px;background:linear-gradient(135deg,#3a3a3a,#d9d6cf)" role="img" aria-label="Veterinarian examining a small dog at a table"></div>
  <div class="photo" style="left:435px;top:2355px;width:330px;height:200px;background:linear-gradient(180deg,#e9ecef,#6c8fb3)" role="img" aria-label="Seminar room with blue chairs facing a projection screen"></div>
  <div class="photo" style="left:797px;top:2355px;width:330px;height:200px;background:linear-gradient(180deg,#f2f2f0,#8b7a68)" role="img" aria-label="Classroom with rows of desks and a projector"></div>

  <h3 class="card-h" style="left:75px;top:2573px">Room Heading</h3>
  <h3 class="card-h" style="left:435px;top:2573px">Room Heading</h3>
  <h3 class="card-h" style="left:797px;top:2573px">Room Heading</h3>
  <p class="card-p" style="left:75px;top:2609px">Sed ut perspiciatis unde omnis iste natus error sit voluptatem accusantium doloremque quaerat.</p>
  <p class="card-p" style="left:435px;top:2609px">Sed ut perspiciatis unde omnis iste natus error sit voluptatem accusantium doloremque quaerat.</p>
  <p class="card-p" style="left:797px;top:2609px">Sed ut perspiciatis unde omnis iste natus error sit voluptatem accusantium doloremque quaerat.</p>
  <div class="btn" style="left:151px;top:2709px;width:179px;height:53px">More Info</div>
  <div class="btn" style="left:511px;top:2709px;width:179px;height:53px">More Info</div>
  <div class="btn" style="left:872px;top:2709px;width:179px;height:53px">More Info</div>
</section>

<section class="accommodation">
  <svg class="abs" style="left:0;top:2826px" width="1200" height="40" viewBox="0 0 1200 40" preserveAspectRatio="none">
    <path d="M0,40 L0,30 C250,30 450,20 600,0 C750,20 950,30 1200,30 L1200,40 Z" fill="#B6EAE3"/>
  </svg>
  <div class="abs" style="left:0;top:2864px;width:1200px;height:518px;background:var(--mint)"></div>
  <div class="photo" style="left:75px;top:2958px;width:513px;height:358px;border-radius:4px;background:linear-gradient(120deg,#b4845f,#d9c8b4 50%,#8b9b8f)" role="img" aria-label="Host welcoming a traveller with a backpack into a guest room"></div>
  <h2 class="abs" style="left:616px;top:2954px;font-size:42px;color:var(--plum);font-weight:700">Accommodation</h2>
  <div class="abs" style="left:616px;top:3020px;width:76px;height:4px;background:var(--teal-deep)"></div>
  <p class="para" style="left:616px;top:3039px;width:512px">Sed ut perspiciatis unde omnis iste natus error sit voluptatem accusantium doloremque laudantium, totam rem aperiam, eaque ipsa quae ab illo inventore veritatis et quasi architecto beatae vitae dicta sunt explicabo. Nemo enim ipsam voluptatem quia voluptas sit aspernatur aut odit aut fugit, sed quia consequuntur magni dolores eos qui ratione voluptatem sequi nesciunt.</p>
  <div class="btn" style="left:616px;top:3257px;width:179px;height:53px">Read More</div>
</section>

<section class="why" role="img" aria-label="Teal tinted photo of a dog and a cat resting under a blanket">
  <h2>WHY CHOOSE US</h2>
  <div class="item" style="left:105px">
    <div class="circle"><svg width="56" height="56" viewBox="0 0 56 56"><g fill="#1B8076"><circle cx="14" cy="22" r="6"/><circle cx="23" cy="12" r="6"/><circle cx="34" cy="12" r="6"/><circle cx="43" cy="22" r="6"/><path d="M28 26c-9 0-16 9-16 16 0 6 7 6 16 6s16 0 16-6c0-7-7-16-16-16z"/></g><path d="M28 33v10M23 38h10" stroke="#fff" stroke-width="3"/></svg></div>
    <div class="label">Lorem ipsum</div>
  </div>
  <div class="item" style="left:369px">
    <div class="circle"><svg width="56" height="56" viewBox="0 0 56 56" fill="none" stroke="#1B8076" stroke-width="3"><rect x="10" y="22" width="36" height="24"/><path d="M8 22h40M20 14h16v8"/><circle cx="24" cy="34" r="5"/><rect x="34" y="30" width="8" height="16"/></svg></div>
    <div class="label">Lorem ipsum</div>
  </div>
  <div class="item" style="left:633px">
    <div class="circle"><svg width="56" height="56" viewBox="0 0 56 56" fill="none" stroke="#1B8076" stroke-width="3"><path d="M14 8v14a8 8 0 0 0 16 0V8"/><path d="M22 30v8a10 10 0 0 0 20 0v-4"/><circle cx="42" cy="30" r="4"/></svg></div>
    <div class="label">Lorem ipsum</div>
  </div>
  <div class="item" style="left:897px">
    <div class="circle"><svg width="56" height="56" viewBox="0 0 56 56" fill="none" stroke="#1B8076" stroke-width="3"><rect x="14" y="6" width="28" height="44" rx="2"/><path d="M20 14h6M30 14h6M20 22h6M30 22h6"/><rect x="22" y="32" width="12" height="12"/></svg></div>
    <div class="label">Lorem ipsum</div>
  </div>
</section>

<section class="testimonials">
  <h2 class="section-title" style="top:3906px">Testimonials</h2>
  <div class="rule" style="top:3973px"></div>

  <svg class="abs" style="left:44px;top:4190px" width="18" height="28" viewBox="0 0 18 28"><path d="M14 2L4 14l10 12" stroke="#7a6f7a" stroke-width="2" fill="none"/></svg>
  <svg class="abs" style="left:1138px;top:4190px" width="18" height="28" viewBox="0 0 18 28"><path d="M4 2l10 12L4 26" stroke="#7a6f7a" stroke-width="2" fill="none"/></svg>

  <div class="tcard" style="left:75px">
    <div class="q">&ldquo;</div>
    <p>But I must explain to you how all this mistaken idea of denouncing pleasure and praising pain was born and I will give you a complete account of the system, and expound the actual teachings of the great explorer of the truth.</p>
    <div class="who"><div class="avatar" role="img" aria-label="Reviewer portrait"></div><div><b>MARTIN</b><small>England</small></div></div>
  </div>
  <div class="tcard" style="left:435px">
    <div class="q">&ldquo;</div>
    <p>But I must explain to you how all this mistaken idea of denouncing pleasure and praising pain was born and I will give you a complete account of the system, and expound the actual teachings of the great explorer of the truth.</p>
    <div class="who"><div class="avatar" role="img" aria-label="Reviewer portrait"></div><div><b>MARTIN</b><small>England</small></div></div>
  </div>
  <div class="tcard" style="left:797px">
    <div class="q">&ldquo;</div>
    <p>But I must explain to you how all this mistaken idea of denouncing pleasure and praising pain was born and I will give you a complete account of the system, and expound the actual teachings of the great explorer of the truth.</p>
    <div class="who"><div class="avatar" role="img" aria-label="Reviewer portrait"></div><div><b>MARTIN</b><small>England</small></div></div>
  </div>
</section>

<footer class="footer">
  <div class="fbrand">
    <div class="mark"></div>
    <div class="name">Veterra<br>Training Center</div>
  </div>

  <h4 style="left:365px">Site Map</h4>
  <ul style="left:365px">
    <li>Home</li><li>About Us</li><li>Rooms</li><li>Book Course</li><li>Accommodation</li><li>Impressum</li><li>Contact Us</li>
  </ul>

  <h4 style="left:605px">Contact Us</h4>
  <div class="copy" style="left:605px;top:114px;width:220px">Neque porro quisquam est,qui dolorem</div>
  <div class="copy" style="left:605px;top:180px">1-800-555-0142</div>
  <div class="copy" style="left:605px;top:214px">info@veterra-academy.com</div>
  <div class="abs" style="left:605px;top:260px;display:flex;gap:18px">
    <span style="width:18px;height:18px;border-radius:50%;background:var(--teal);display:block"></span>
    <span style="width:18px;height:18px;border-radius:50%;background:var(--teal);display:block"></span>
    <span style="width:18px;height:18px;border-radius:50%;background:var(--teal);display:block"></span>
    <span style="width:18px;height:18px;border-radius:50%;background:var(--teal);display:block"></span>
    <span style="width:18px;height:18px;border-radius:50%;background:var(--teal);display:block"></span>
  </div>

  <h4 style="left:885px">Email Subscribe</h4>
  <div class="copy" style="left:885px;top:114px;width:240px">Neque porro quisquam est, qui dolorem</div>
  <div class="input">Email Address</div>
  <div class="btn" style="left:885px;top:230px;width:242px;height:46px;font-size:20px">Subscribe</div>
</footer>

</body>
</html>
```